New one page Homepage with registration and log in form

Hi designers!

We need a new homepage and made a skitch of how it should be.

Can you give some of your design ideas and work it out so that it actually looks great?

Its just one page, for convertion reasons.

The logo doesnt have to be changed.

It would be cool to center the logo but not sure how design technically correct that is.

The social icons can be left out.

If you could give a few mockups than we can choose the best one.

I added one screenshot sketch of the homepage.

And 2 screenshots of what the system looks like on the inside, just so you get an idea.

Thanks

Target Market(s)

Vacation rental owners who want to increase their bookings by connecting with other VR owners and managers, or by having their own booking team for a small fee.

Industry/Entity Type

Social

Number of Pages Required

1 page

Requirements
Must have
• Use your imagination please
Nice to have
• Use your imagination
• It will be a one page design so we need to impress :)
• Keep it compact, maybe a web 3.0 flat design, etc
Should not have
• Other pages.

```html
<!DOCTYPE html>
<html lang="en">
<head>
<meta charset="utf-8">
<title>StayNest – The First Social Booking Network</title>
<link href="https://fonts.googleapis.com/css2?family=Source+Sans+3:wght@400;600;700&family=Arimo:wght@400;700&display=swap" rel="stylesheet">
<style>
:root{
  --blue:#0349a8;
  --blue-dark:#003c95;
  --orange:#f26a10;
  --orange-btn:#fb6a12;
  --page-bg:#e8e8e8;
  --white:#ffffff;
  --panel:#f0f0f0;
  --ink:#1a1a1a;
  --field-border:#c9c9c9;
  --placeholder:#8a8a8a;
}
*{box-sizing:border-box;margin:0;padding:0}
html,body{width:1200px;height:1127px;overflow:hidden}
body{background:var(--page-bg);font-family:"Arimo",Arial,sans-serif;color:var(--ink);position:relative}
.site-header{position:absolute;left:0;top:0;width:1200px;height:139px;background:var(--white)}
.brand{position:absolute;left:106px;top:38px;display:flex;align-items:center;gap:10px}
.brand-square{width:40px;height:40px;background:var(--blue)}
.brand-name{font-family:"Source Sans 3",sans-serif;font-weight:700;font-size:40px;color:var(--blue);line-height:1}
.social-links{position:absolute;left:953px;top:59px;display:flex;gap:9px}
.social-dot{width:36px;height:36px;border-radius:50%}
.dot-a{background:#3b5a9a}.dot-b{background:#1da1e2}.dot-c{background:#d4291f}
.main-card{position:absolute;left:100px;top:152px;width:1000px;height:975px;background:var(--white)}
.nav-bar{position:absolute;left:10px;top:13px;width:980px;height:51px;background:var(--blue-dark);border-radius:14px}
.nav-lock{position:absolute;right:0;top:0;width:58px;height:51px;border-left:1px solid #1b4fa0;display:flex;align-items:center;justify-content:center}
.headline{position:absolute;left:0;top:86px;width:1000px;text-align:center;font-family:"Source Sans 3",sans-serif;font-size:40px;color:var(--orange);font-weight:400}
.video{position:absolute;left:19px;top:161px;width:411px;height:250px;border:3px solid var(--blue-dark);background:linear-gradient(135deg,#d9d2c6,#b9aa98 45%,#6f6a6d);}
.video-play{position:absolute;left:178px;top:94px;width:52px;height:52px;border-radius:50%;border:2px solid rgba(255,255,255,.8);background:rgba(0,0,0,.25)}
.video-play::after{content:"";position:absolute;left:19px;top:14px;border-left:18px solid rgba(255,255,255,.85);border-top:11px solid transparent;border-bottom:11px solid transparent}
.video-controls{position:absolute;left:8px;top:209px;width:392px;height:28px;border-radius:8px;background:rgba(20,20,25,.8)}
.video-track{position:absolute;left:60px;top:13px;width:120px;height:2px;background:#ddd}
.intro{position:absolute;left:483px;top:159px;width:470px;font-size:14px;line-height:18px}
.intro p{margin-bottom:18px}
.account-band{position:absolute;left:0;top:458px;width:1000px;height:517px;background:var(--blue)}
.login{position:absolute;left:16px;top:0;width:387px}
.login-title{margin-top:42px;text-align:center;font-family:"Source Sans 3",sans-serif;font-weight:400;font-size:35px;color:var(--white)}
.field{display:block;width:100%;height:35px;background:var(--white);border:1px solid var(--field-border);border-radius:3px;padding:0 10px;font:14px "Arimo",Arial,sans-serif;color:var(--placeholder);line-height:33px}
.login .field{height:35px}
.login .field-user{position:absolute;top:99px}
.login .field-pass{position:absolute;top:153px}
.remember{position:absolute;top:210px;left:3px;display:flex;align-items:center;gap:14px;color:var(--white);font-size:15px}
.remember-box{width:24px;height:21px;background:var(--white);border:3px solid var(--orange-btn)}
.btn-login{position:absolute;top:253px;left:0;width:387px;height:44px;border-radius:4px;background:var(--orange-btn);color:var(--white);font-family:"Source Sans 3",sans-serif;font-weight:600;font-size:19px;text-align:center;line-height:44px}
.social-label{position:absolute;top:315px;left:0;width:414px;text-align:center;color:var(--white);font-size:15px}
.btn-social{position:absolute;top:357px;left:88px;width:242px;height:55px;border-radius:7px;background:linear-gradient(#3c8fdc,#1e6fc6);border:1px solid #155bb0;display:flex;align-items:center;color:var(--white);font-weight:700;font-size:15px}
.btn-social-square{width:16px;height:16px;background:var(--white);margin:0 14px 0 16px}
.btn-social-divider{width:1px;height:38px;background:#6aa9e8;margin-right:10px}
.forgot{position:absolute;top:438px;left:0;width:420px;text-align:center;color:var(--orange-btn);font-size:13px}
.register{position:absolute;left:451px;top:11px;width:540px;height:495px;background:var(--panel)}
.register-title{margin-top:14px;text-align:center;font-family:"Source Sans 3",sans-serif;font-weight:700;font-size:28px;color:var(--orange)}
.register-sub{text-align:center;font-size:12px;margin-top:4px}
.register .field{position:absolute;height:36px;border:2px solid #d2d2d2;border-radius:4px}
.f-first{left:13px;top:88px;width:245px!important}
.f-last{left:277px;top:88px;width:245px!important}
.f-user{left:14px;top:143px;width:509px!important}
.f-pass{left:14px;top:199px;width:509px!important}
.f-mail{left:14px;top:255px;width:509px!important}
.f-phone{left:14px;top:310px;width:509px!important}
.f-reason{left:14px;top:368px;width:509px!important}
.terms{position:absolute;left:0;top:433px;width:540px;text-align:center;color:var(--orange-btn);font-size:13.5px;line-height:16px}
</style>
</head>
<body>
<header class="site-header">
  <div class="brand"><span class="brand-square"></span><span class="brand-name">StayNest</span></div>
  <nav class="social-links" aria-label="Social links">
    <span class="social-dot dot-a"></span><span class="social-dot dot-b"></span><span class="social-dot dot-c"></span>
  </nav>
</header>

<main class="main-card">
  <div class="nav-bar">
    <div class="nav-lock">
      <svg width="14" height="18" viewBox="0 0 14 18" aria-hidden="true"><path d="M3 8V5a4 4 0 0 1 8 0v3" fill="none" stroke="#fff" stroke-width="2.2"/><rect x="1" y="8" width="12" height="9" rx="1.5" fill="#fff"/><circle cx="7" cy="12.5" r="1.6" fill="#003c95"/></svg>
    </div>
  </div>

  <h1 class="headline">The First Social Booking Network</h1>

  <div class="video" role="img" aria-label="Intro video still: a family sharing tablets on a sofa">
    <span class="video-play"></span>
    <div class="video-controls"><span class="video-track"></span></div>
  </div>

  <div class="intro">
    <p>StayNest is a new Social Booking Network.</p>
    <p>Vacation rental hosts and Property Managers can find easch other, connect and chat amongst themselves for sharing reservation inquires, services or anything you can imagine, in a convenient social environ-ment.</p>
    <p>Managers can find easch other, connect and chat amongst themselves for sharing reservation inquires, services or anything you can imagine, in a convenient social environment.</p>
    <p>Vacation rental hosts and Property Managers can find easch other, connect and chat amongst themselves for sharing reservation inquires, services or anything you can imagine.</p>
  </div>

  <section class="account-band">
    <div class="login">
      <h2 class="login-title">Login to Your account</h2>
      <div class="field field-user">Your username or email address</div>
      <div class="field field-pass">Your Password</div>
      <div class="remember"><span class="remember-box"></span>Would You Like Us to remember You?</div>
      <div class="btn-login">Log Me In</div>
      <div class="social-label">Sign in With Your Social identity</div>
      <div class="btn-social"><span class="btn-social-square"></span><span class="btn-social-divider"></span>Sign in With Chatterly</div>
      <div class="forgot">I forgot my username / password</div>
    </div>

    <div class="register">
      <h2 class="register-title">Don’t have an account?</h2>
      <p class="register-sub">Register now to join the Free Booking Network !</p>
      <div class="field f-first">First Name</div>
      <div class="field f-last">Last Name</div>
      <div class="field f-user">Username</div>
      <div class="field f-pass">Password</div>
      <div class="field f-mail">user@email.com</div>
      <div class="field f-phone">Set your contact number. Example: +12345678910</div>
      <div class="field f-reason">Whats your reason for joining?</div>
      <p class="terms">Thank you for choosing StayNest, and for using our serices<br>("Serives"). The StayNest serices are provided by Velmora S.A.</p>
    </div>
  </section>
</main>
</body>
</html>
```